Develop a PowerPoint template based on existing logo for a non-profit international alliance of professionals.
Presentations that will be made with this template will include mostly bullet point text and some tables. SOme images could also be included.

Target Market(s)

Governments, private funders

Industry/Entity Type

Non-Profit

Requirements
Must have
• clean and modern feel
Should not have
• no background in the slide area

```html
<!DOCTYPE html>
<html lang="en">
<head>
<meta charset="utf-8">
<title>Meridian Innovation Alliance – Slide Template</title>
<link rel="stylesheet" href="https://fonts.googleapis.com/css2?family=Tinos:wght@400;700&display=swap">
<style>
  :root {
    --brand-red: #e3202a;
    --brand-red-dark: #c4151e;
    --slide-light: #fbfbfb;
    --slide-shade: #e9e9e9;
    --text-body: #1e1e1e;
    --frame-border: #a9a9a9;
    --placeholder-light: #ffffff;
    --placeholder-mid: #e4e4e4;
    --divider: #cfcfcf;
  }
  html, body {
    margin: 0;
    padding: 0;
    width: 1200px;
    height: 844px;
    overflow: hidden;
    background: #ffffff;
  }
  .slide {
    position: relative;
    width: 1200px;
    height: 844px;
    background: radial-gradient(ellipse at 35% 30%, var(--slide-light) 0%, #f3f3f3 55%, var(--slide-shade) 100%);
    font-family: "Tinos", "Times New Roman", serif;
    color: var(--text-body);
    overflow: hidden;
  }
  .brand {
    position: absolute;
    left: 150px;
    top: 122px;
    display: flex;
    align-items: center;
    gap: 14px;
  }
  .brand-dot {
    width: 40px;
    height: 40px;
    border-radius: 50%;
    background: var(--brand-red);
  }
  .brand-name {
    font-family: "Tinos", "Times New Roman", serif;
    font-weight: 700;
    font-size: 30px;
    color: var(--brand-red);
    letter-spacing: 0.2px;
  }
  .content-divider {
    position: absolute;
    left: 320px;
    top: 250px;
    width: 2px;
    height: 478px;
    background: linear-gradient(to bottom, rgba(207,207,207,0) 0%, var(--divider) 30%, var(--divider) 70%, rgba(207,207,207,0) 100%);
  }
  .feature {
    position: absolute;
    left: 359px;
    width: 740px;
  }
  .feature--first { top: 238px; }
  .feature--second { top: 506px; }
  .feature-heading {
    margin: 0 0 21px 0;
    font-weight: 700;
    font-size: 28px;
    line-height: 1.2;
    color: var(--brand-red);
  }
  .feature-row {
    display: flex;
    align-items: flex-start;
    gap: 20px;
  }
  .picture-frame {
    flex: 0 0 auto;
    width: 334px;
    height: 160px;
    box-sizing: border-box;
    border: 2px solid var(--frame-border);
    background: #f7f7f7;
    padding: 8px;
  }
  .picture-placeholder {
    width: 100%;
    height: 100%;
    background: radial-gradient(ellipse at 50% 50%, var(--placeholder-light) 0%, #eeeeee 45%, var(--placeholder-mid) 100%);
  }
  .feature-text {
    margin: -4px 0 0 0;
    width: 381px;
    font-size: 18.5px;
    line-height: 24px;
    text-align: justify;
  }
  .footer-band {
    position: absolute;
    left: 0;
    bottom: 0;
    width: 1200px;
    height: 35px;
    background: linear-gradient(to bottom, var(--brand-red) 0%, var(--brand-red) 55%, var(--brand-red-dark) 100%);
  }
</style>
</head>
<body>
  <main class="slide">
    <header class="brand">
      <span class="brand-dot" aria-hidden="true"></span>
      <span class="brand-name">Meridian Innovation Alliance</span>
    </header>

    <div class="content-divider" aria-hidden="true"></div>

    <section class="feature feature--first">
      <h2 class="feature-heading">Picture with heading 1</h2>
      <div class="feature-row">
        <div class="picture-frame">
          <div class="picture-placeholder" role="img" aria-label="Placeholder area for a slide picture"></div>
        </div>
        <p class="feature-text">Lorem Ipsum is simply dummy text of the printing and typesetting industry. Lorem Ipsum has been the industry's standard dummy text ever since the 1500s, when an unknown printer took a galley of type and scrambled it to make a type specimen book. It has survived not only five centuries.</p>
      </div>
    </section>

    <section class="feature feature--second">
      <h2 class="feature-heading">Picture with heading 2</h2>
      <div class="feature-row">
        <div class="picture-frame">
          <div class="picture-placeholder" role="img" aria-label="Placeholder area for a slide picture"></div>
        </div>
        <p class="feature-text">Lorem Ipsum is simply dummy text of the printing and typesetting industry. Lorem Ipsum has been the industry's standard dummy text ever since the 1500s, when an unknown printer took a galley of type and scrambled it to make a type specimen book. It has survived not only five centuries.</p>
      </div>
    </section>

    <div class="footer-band" aria-hidden="true"></div>
  </main>
</body>
</html>
```